Beacon Advisory Website

I currently have a website www.beaconadvisoryinc.example. We are a IT Consulting Company. Our website will pretty much tell out our services. I am looking to enhance my website and make it look more professional. Looking for very classy and Contemporary look and design for my website.

Industry/Entity Type

It Company

```html
<!DOCTYPE html>
<html lang="en">
<head>
<meta charset="utf-8">
<title>Beacon Advisory</title>
<link rel="stylesheet" href="https://fonts.googleapis.com/css2?family=Roboto:wght@300;400;500;700;900&family=Open+Sans:wght@400;600&display=swap">
<style>
:root{
  --blue:#1a9ae0;
  --blue-dark:#0d5f98;
  --navy:#0f3e66;
  --green:#5aab3c;
  --orange:#f26522;
  --teal:#2aa3e0;
  --charcoal:#3a3d42;
  --ink:#333;
  --muted:#6b6b6b;
  --light:#f1f2f4;
  --footer:#2b2c2e;
  --footer-deep:#1f2022;
  --white:#fff;
}
*{box-sizing:border-box;margin:0;padding:0}
html,body{width:1200px;height:2472px;overflow:hidden}
body{font-family:"Open Sans",sans-serif;color:var(--ink);background:var(--white);position:relative}
h1,h2,h3,h4,.nav a,.btn{font-family:"Roboto",sans-serif}

.topbar{height:32px;background:var(--blue-dark);color:var(--white);font-size:12px;display:flex;align-items:center;padding:0 60px;justify-content:space-between}
.topbar .contact span{margin-right:24px}
.topbar .follow{display:flex;align-items:center;gap:10px}
.topbar .dot{width:16px;height:16px;border-radius:50%;background:rgba(255,255,255,.35)}

.header{height:112px;display:flex;align-items:center;justify-content:space-between;padding:0 60px;background:var(--white)}
.brand{display:flex;align-items:center;gap:12px}
.brand .mark{width:44px;height:44px;border-radius:50%;background:var(--blue)}
.brand .name{font-family:"Roboto",sans-serif;font-weight:700;font-size:26px;color:var(--blue-dark)}
.nav{display:flex;gap:34px}
.nav a{font-size:13px;font-weight:500;color:var(--ink);text-decoration:none;letter-spacing:.5px;padding:8px 0}
.nav a.active{color:var(--blue);border-top:2px solid var(--blue)}

.hero{position:relative;height:544px;background:linear-gradient(90deg,#e9ecef 0%,#f7f8f9 45%,#cfd6de 100%);overflow:hidden}
.hero .photo{position:absolute;right:0;top:0;width:620px;height:544px;background:linear-gradient(160deg,#dfe4ea 0%,#5e6b7a 55%,#1e2a38 100%)}
.hero .headline{position:absolute;left:80px;top:230px}
.hero .band{background:var(--charcoal);color:var(--white);padding:14px 22px;display:inline-block}
.hero .band h2{font-size:30px;font-weight:700;letter-spacing:.5px}
.hero .band p{font-size:13px;letter-spacing:1px;margin-top:4px;font-weight:600}
.hero .tagline{margin-top:18px;background:rgba(58,61,66,.9);color:var(--white);padding:12px 22px;display:inline-block;font-family:"Roboto",sans-serif}
.hero .tagline p{font-size:13px;letter-spacing:.8px}
.hero .tagline strong{font-size:28px;color:var(--teal);font-weight:900;margin-right:8px}

.welcome{height:312px;padding:40px 60px 0;position:relative}
.welcome h1{font-size:30px;font-weight:500;color:var(--ink);display:flex;align-items:center;gap:12px}
.welcome h1 .mark{width:30px;height:30px;border-radius:50%;background:var(--blue)}
.welcome .copy{width:600px;margin-top:18px;font-size:13px;line-height:1.6;color:var(--muted)}
.welcome .copy p{margin-bottom:8px}
.btn{display:inline-block;background:var(--blue-dark);color:var(--white);font-size:12px;font-weight:500;padding:9px 16px;letter-spacing:.5px;margin-top:6px}
.welcome .devices{position:absolute;right:120px;top:40px;width:320px;height:200px;background:linear-gradient(135deg,#e6eaee,#8c98a6);border-radius:6px}

.services{height:360px;background:var(--light);padding-top:40px}
.section-title{text-align:center;font-size:26px;font-weight:700;letter-spacing:1px}
.section-title::after{content:"";display:block;width:50px;height:3px;background:var(--blue);margin:10px auto 0}
.cards{display:flex;gap:16px;padding:0 60px;margin-top:30px}
.card{flex:1;height:208px;background:var(--white)}
.card .img{height:96px}
.card .body{height:112px;padding:12px 14px;color:var(--white)}
.card h3{font-size:13px;font-weight:700;letter-spacing:.4px;text-align:right}
.card p{font-size:11px;line-height:1.5;margin-top:6px}
.card .more{font-family:"Roboto",sans-serif;font-size:10px;font-weight:700;margin-top:6px;display:block}
.card.orange .body{background:var(--orange)} .card.orange .img{background:linear-gradient(135deg,#8a5a3a,#2c2c2c)}
.card.blue .body{background:#1c8fd6} .card.blue .img{background:linear-gradient(135deg,#bcd6ea,#3f6f94)}
.card.teal .body{background:var(--teal)} .card.teal .img{background:linear-gradient(135deg,#e8eef3,#5a8fb3)}
.card.green .body{background:var(--green)} .card.green .img{background:linear-gradient(135deg,#50606c,#16222c)}
.card.gray .body{background:var(--charcoal)} .card.gray .img{background:linear-gradient(135deg,#8fb7d8,#2f5878)}

.process{height:400px;background:var(--blue);position:relative;color:var(--white);padding-top:40px}
.process .section-title{color:var(--navy)}
.process .section-title::after{background:var(--white)}
.process svg{position:absolute;left:0;top:0}
.step{position:absolute;width:220px;text-align:center;font-size:11px;line-height:1.5}
.step h4{position:absolute;left:0;right:0;font-size:18px;font-weight:700;letter-spacing:.5px}

.testimonials{height:368px;padding-top:40px}
.quotes{display:flex;gap:40px;padding:0 60px;margin-top:36px}
.quote{flex:1;display:flex;gap:14px}
.quote .portrait{width:84px;height:104px;flex:none;background:linear-gradient(180deg,#d7dbe0,#6f7a86)}
.quote p{font-size:11px;line-height:1.6;color:var(--muted)}
.quote p::before{content:"\201C";font-family:"Roboto",sans-serif;font-size:30px;color:var(--blue);line-height:0;vertical-align:-10px;margin-right:4px}
.quote .who{margin-top:10px;font-family:"Roboto",sans-serif;font-size:11px;font-weight:700;color:var(--blue)}
.quote .role{font-size:11px;color:var(--ink)}

.footer{height:304px;background:var(--footer);color:#c9c9c9;display:flex;padding:40px 60px 0;gap:40px}
.footer .col{width:260px}
.footer h4{color:var(--white);font-size:16px;font-weight:700;letter-spacing:1px;padding-bottom:12px;border-bottom:1px solid #444;margin-bottom:16px}
.footer p{font-size:13px;line-height:1.7}
.footer .socials{display:flex;gap:10px}
.footer .socials span{width:26px;height:26px;border-radius:50%;background:var(--blue)}
.copyright{height:40px;background:var(--footer-deep);color:#8a8a8a;font-size:11px;display:flex;align-items:center;justify-content:center}
</style>
</head>
<body>

<div class="topbar">
  <div class="contact"><span>+1 (555) 014 2290</span><span>info@beaconadvisoryinc.example</span></div>
  <div class="follow"><span>Follow us</span><span class="dot"></span><span class="dot"></span><span class="dot"></span></div>
</div>

<header class="header">
  <div class="brand"><span class="mark"></span><span class="name">Beacon Advisory</span></div>
  <nav class="nav">
    <a class="active">COMPANY</a><a>SERVICES</a><a>SOLUTIONS</a><a>RESOURCES</a><a>CAREER</a><a>CONTACT US</a>
  </nav>
</header>

<section class="hero">
  <div class="photo" role="img" aria-label="Business professional holding a tablet with glowing data charts"></div>
  <div class="headline">
    <div class="band">
      <h2>ATTRACTING AND DEVELOPING</h2>
      <p>THE BEST TALENT FOR OUR BUSINESS</p>
    </div><br>
    <div class="tagline">
      <p>STRETCHING OUR PEOPLE AND DEVELOPING</p>
      <p>A <strong>"CAN DO"</strong>ATTITUDE</p>
    </div>
  </div>
</section>

<section class="welcome">
  <h1><span class="mark"></span>Welcome to Beacon Advisory</h1>
  <div class="copy">
    <p>Through the commitment of our employees and innovative engineering, we provide highly reliable, flexible services, solutions and integrated products that maximize our customers' competitive advantage.</p>
    <p>Delivering real value to our clients by providing top quality technical services and solutions at reasonable rates.</p>
    <p>Delivering real value to shareholders through consistent growth and strong profitability, delivering the best work environment for our consultants and staff.</p>
    <span class="btn">READ MORE</span>
  </div>
  <div class="devices" role="img" aria-label="Laptop, tablet and phone showing the website"></div>
</section>

<section class="services">
  <h2 class="section-title">OUR SERVICES</h2>
  <div class="cards">
    <div class="card orange"><div class="img" role="img" aria-label="Technology workspace photo"></div><div class="body"><h3>TECHNOLOGY</h3><p>Lorem ipsum dolor sit amet, consectetur adipiscing elit sed do.</p><span class="more">READ MORE ›</span></div></div>
    <div class="card blue"><div class="img" role="img" aria-label="Business meeting photo"></div><div class="body"><h3>BUSINESS</h3><p>Lorem ipsum dolor sit amet, consectetur adipiscing elit sed do.</p><span class="more">READ MORE ›</span></div></div>
    <div class="card teal"><div class="img" role="img" aria-label="Application icons illustration"></div><div class="body"><h3>APPLICATION DEVELOPMENT</h3><p>Lorem ipsum dolor sit amet, consectetur adipiscing elit sed do.</p><span class="more">READ MORE ›</span></div></div>
    <div class="card green"><div class="img" role="img" aria-label="Network integration photo"></div><div class="body"><h3>ENTERPRISE INTEGRATION</h3><p>Lorem ipsum dolor sit amet, consectetur adipiscing elit sed do.</p><span class="more">READ MORE ›</span></div></div>
    <div class="card gray"><div class="img" role="img" aria-label="Consultant using touch screen photo"></div><div class="body"><h3>IT CONSULTING</h3><p>Lorem ipsum dolor sit amet, consectetur adipiscing elit sed do.</p><span class="more">READ MORE ›</span></div></div>
  </div>
</section>

<section class="process">
  <svg width="1200" height="400" viewBox="0 0 1200 400" aria-hidden="true">
    <path d="M330 170 Q460 110 600 240 Q740 110 870 170" fill="none" stroke="#fff" stroke-width="3" stroke-dasharray="6 6"/>
    <circle cx="330" cy="170" r="72" fill="#fff" opacity=".35"/>
    <circle cx="330" cy="170" r="62" fill="var(--navy)"/>
    <circle cx="600" cy="240" r="92" fill="#fff" opacity=".35"/>
    <circle cx="600" cy="240" r="82" fill="var(--green)"/>
    <circle cx="870" cy="170" r="72" fill="#fff" opacity=".35"/>
    <circle cx="870" cy="170" r="62" fill="var(--navy)"/>
  </svg>
  <h2 class="section-title" style="position:relative">OUR PROCESS</h2>
  <div class="step" style="left:220px;top:160px"><h4 style="top:0">EXAMINE</h4><p style="margin-top:100px">Consectetur adipiscing elit, sed diam nonummy nibh euismod tincidunt.</p></div>
  <div class="step" style="left:490px;top:229px"><h4 style="top:0">UNDERSTAND</h4><p style="margin-top:120px">Consectetur adipiscing elit, sed diam nonummy nibh euismod tincidunt.</p></div>
  <div class="step" style="left:760px;top:160px"><h4 style="top:0">DELIVER</h4><p style="margin-top:100px">Consectetur adipiscing elit, sed diam nonummy nibh euismod tincidunt.</p></div>
</section>

<section class="testimonials">
  <h2 class="section-title">TESTIMONIALS</h2>
  <div class="quotes">
    <div class="quote"><div class="portrait" role="img" aria-label="Client portrait"></div><div><p>Consectetur adipiscing elit, sed diam nonummy nibh euismod tincidunt ut laoreet dolore magna aliquam erat volutpat. Ut wisi enim ad minim veniam, quis nostrud exerci tation.</p><div class="who">Lorem Ipsum Dolor</div><div class="role">Managing Director</div></div></div>
    <div class="quote"><div class="portrait" role="img" aria-label="Client portrait"></div><div><p>Consectetur adipiscing elit, sed diam nonummy nibh euismod tincidunt ut laoreet dolore magna aliquam erat volutpat. Ut wisi enim ad minim veniam, quis nostrud exerci tation.</p><div class="who">Lorem Ipsum Dolor</div><div class="role">Managing Director</div></div></div>
    <div class="quote"><div class="portrait" role="img" aria-label="Client portrait"></div><div><p>Consectetur adipiscing elit, sed diam nonummy nibh euismod tincidunt ut laoreet dolore magna aliquam erat volutpat. Ut wisi enim ad minim veniam, quis nostrud exerci tation.</p><div class="who">Lorem Ipsum Dolor</div><div class="role">Managing Director</div></div></div>
  </div>
</section>

<footer class="footer">
  <div class="col"><h4>ADDRESS</h4><p>Level 7, 12 Harbour Street,<br>Riverton, NSW 2000</p></div>
  <div class="col"><h4>PHONE</h4><p>+1 (555) 014 2290</p></div>
  <div class="col"><h4>EMAIL</h4><p>info@beaconadvisoryinc.example</p></div>
  <div class="col"><h4>FOLLOW US</h4><div class="socials"><span></span><span></span><span></span><span></span><span></span></div></div>
</footer>
<div class="copyright">Copyright © Beacon Advisory</div>

</body>
</html>
```